Mobile dental anesthesiologist needs a postcard to market to other doctors

This postcard is intended to inform dentists in the California Central Coast region that I am available to travel to their office to serve their patient's anesthesia needs. It is important to know that other anesthesiologists are usually booked for weeks in advance and are very costly. Our market niche is greater availability and lower cost. I would prefer a 2 sided oversized postcard. The attached images are DIY projects I've done recently...You can see why I'm reaching out to professionals.

Industry/Entity Type

Dental

```html
<!DOCTYPE html>
<html lang="en">
<head>
<meta charset="utf-8">
<title>Seaside Mobile Dental Anesthesia – Postcard</title>
<link href="https://fonts.googleapis.com/css2?family=Didact+Gothic&family=Arimo:wght@700&display=swap" rel="stylesheet">
<style>
  :root {
    --page: #ffffff;
    --ink-dark: #3f3e55;
    --panel-dark: #3f3e55;
    --band-grey: #9e9eab;
    --card-grey: #c4c4cc;
    --teal: #3d8a85;
    --teal-light: #8fb8bd;
    --lilac: #c9c8e6;
    --purple-text: #4c4a78;
    --stripe: #4d4a8c;
    --caption-bg: #b9d3d4;
    --white: #ffffff;
  }
  * { box-sizing: border-box; margin: 0; padding: 0; }
  html, body { width: 930px; height: 1200px; overflow: hidden; background: var(--page); }
  body { font-family: "Didact Gothic", sans-serif; color: var(--ink-dark); position: relative; }

  .card { position: absolute; left: 20px; width: 890px; height: 572px; overflow: hidden; }
  .card--front { top: 20px; background: var(--band-grey); }
  .card--back { top: 608px; background: var(--card-grey); }

  /* Front */
  .front-photo { position: absolute; left: 0; top: 0; width: 620px; height: 408px;
    background: linear-gradient(120deg, #cfe3df 0%, #8ec9cc 35%, #e9e4e0 60%, #b7d6dc 100%); }
  .front-shapes { position: absolute; inset: 0; }
  .front-pitch { position: absolute; left: 588px; top: 38px; width: 296px;
    font-variant: small-caps; color: var(--white); font-size: 25px; line-height: 30px; white-space: nowrap; }
  .front-pitch em { font-style: italic; }
  .benefits { list-style: none; position: absolute; left: 602px; top: 212px;
    font-variant: small-caps; color: var(--lilac); font-size: 25px; line-height: 29px; white-space: nowrap; }
  .benefits li::before { content: "♦"; font-size: 10px; margin-right: 16px; vertical-align: 4px; color: var(--lilac); }
  .front-call { position: absolute; left: 624px; top: 412px; width: 260px;
    color: var(--white); font-size: 18px; line-height: 23px; white-space: nowrap; }
  .front-phone { position: absolute; left: 624px; top: 488px; width: 254px; text-align: center;
    font-family: "Arimo", sans-serif; font-weight: 700; font-size: 32px; color: var(--teal-light); }

  .brand { text-align: center; }
  .brand-name { color: var(--teal); font-size: 40px; letter-spacing: 1px; line-height: 1.15; }
  .brand-line { color: var(--ink-dark); font-size: 28px; letter-spacing: .5px; line-height: 1.2; }
  .brand-tag { color: var(--purple-text); font-style: italic; font-size: 20px; line-height: 1.3; }
  .front-brand { position: absolute; left: 20px; top: 412px; width: 580px; }
  .front-serving { position: absolute; left: 20px; top: 542px; width: 580px; text-align: center;
    color: var(--teal); font-style: italic; font-size: 17px; }

  /* Back */
  .back-brand { position: absolute; left: 20px; top: 18px; width: 467px; }
  .back-brand .brand-name { font-size: 30px; }
  .back-brand .brand-line { font-size: 20px; }
  .back-brand .brand-tag { font-size: 15px; }
  .rule-band { position: absolute; left: 20px; width: 472px; height: 19px; background: var(--stripe); }
  .rule-band--top { top: 119px; }
  .rule-band--bottom { top: 398px; }
  .portrait { position: absolute; left: 22px; top: 144px; width: 184px; height: 202px;
    background: radial-gradient(circle at 50% 40%, #9a9a9a, #2b2b2b 75%); }
  .portrait-caption { position: absolute; left: 22px; top: 346px; width: 184px; height: 48px;
    background: var(--caption-bg); text-align: center; font-size: 12px; line-height: 19px;
    padding-top: 5px; color: #2c2c2c; font-weight: bold; }
  .bio { position: absolute; left: 218px; top: 148px; width: 266px; font-size: 12.5px; line-height: 16.4px; color: #2c2c2c; }
  .bio p + p { margin-top: 9px; }
  .back-contact { position: absolute; left: 20px; top: 424px; width: 472px; text-align: center; }
  .back-invite { color: var(--purple-text); font-size: 21px; line-height: 27px; }
  .back-phone { margin-top: 10px; font-family: "Arimo", sans-serif; font-weight: 700; font-size: 26px; color: var(--ink-dark);
    display: flex; justify-content: center; align-items: center; gap: 10px; }
  .back-email { margin-top: 10px; font-size: 16px; color: var(--ink-dark);
    display: flex; justify-content: center; align-items: center; gap: 8px; }
</style>
</head>
<body>

<section class="card card--front">
  <div class="front-photo" role="img" aria-label="Photo of a startled woman in a dental chair covering her mouth while gloved hands hold dental tools"></div>
  <svg class="front-shapes" width="890" height="572" viewBox="0 0 890 572" aria-hidden="true">
    <polygon points="552,0 890,0 890,572 620,572 598,408" fill="var(--panel-dark)"/>
  </svg>

  <p class="front-pitch">Put your patients and<br>their families at ease by<br>offering safe and<br>effective anesthesia in the<br><em>comfort of your office:</em></p>
  <ul class="benefits">
    <li>Expert Care</li>
    <li>Hospital Standards</li>
    <li>Simple Billing</li>
    <li>Easy Flexible Scheduling</li>
    <li>Lower Cost</li>
  </ul>
  <p class="front-call">Call to schedule a discussion<br>of how mobile anesthesia<br>may benefit your practice!</p>
  <p class="front-phone">555.014.2290</p>

  <div class="brand front-brand">
    <p class="brand-name">Seaside</p>
    <p class="brand-line">MOBILE DENTAL ANESTHESIA</p>
    <p class="brand-tag">Opening Paths to Care</p>
  </div>
  <p class="front-serving">Serving the Bay Region from Harbor Point to Pine Ridge</p>
</section>

<section class="card card--back">
  <div class="brand back-brand">
    <p class="brand-name">Seaside</p>
    <p class="brand-line">MOBILE DENTAL ANESTHESIA</p>
    <p class="brand-tag">Opening Paths to Care</p>
  </div>

  <div class="rule-band rule-band--top"></div>
  <div class="portrait" role="img" aria-label="Black and white portrait of the dentist anesthesiologist in suit and tie"></div>
  <p class="portrait-caption">Daniel Hale, DDS<br>Anesthesiologist</p>
  <div class="bio">
    <p>Dr. Daniel Hale is a Dentist Anesthesiologist with experience in treating patients with a wide spectrum of ages and conditions.</p>
    <p>Dr. Hale received his Doctor of Dental Surgery from Lakeview University College of Dentistry in 2004, prior to running his own private general dentistry practice that used IV sedation. In 2013, Dr. Hale completed a residency in dental anesthesiology at Northfield College of Medicine/ Riverside Medical Center. Based in a Level I trauma center, this residency served as rigorous preparation for private practice.</p>
  </div>
  <div class="rule-band rule-band--bottom"></div>

  <div class="back-contact">
    <p class="back-invite">Contact me for a discussion of how mobile<br>anesthesia may benefit your practice!</p>
    <p class="back-phone">
      <svg width="12" height="20" viewBox="0 0 12 20" aria-hidden="true"><rect x="1" y="1" width="10" height="18" rx="2" fill="none" stroke="var(--teal)" stroke-width="2"/><line x1="4" y1="15" x2="8" y2="15" stroke="var(--teal)" stroke-width="2"/></svg>
      555.014.2290
    </p>
    <p class="back-email">
      <svg width="18" height="13" viewBox="0 0 18 13" aria-hidden="true"><rect x="1" y="1" width="16" height="11" fill="none" stroke="var(--purple-text)" stroke-width="1.5"/><polyline points="1,1 9,7 17,1" fill="none" stroke="var(--purple-text)" stroke-width="1.5"/></svg>
      DHALE.DDS@EXAMPLE.COM
    </p>
  </div>
</section>

</body>
</html>
```